professional business card

A Clean looking business card for a money transfer company. Our company is call Velorix= Transfer + Send = Transcend (next level)
to show professionalism as well as some effects to show digital tech.

1 side to have position, name and address
2 side to have company name and show that we provide money exchange and cross-border money transfer

Target Market(s)

Remittance companies and high net worth individuals

Industry/Entity Type

Finance

Contact Information for Business Card

Name, address, email, title, services- money exchange and cross-border remittance

Requirements
Nice to have
• Digital age feel

```html
<!DOCTYPE html>
<html lang="en">
<head>
<meta charset="utf-8">
<title>Velorix Business Card</title>
<link rel="stylesheet" href="https://fonts.googleapis.com/css2?family=Montserrat:wght@600&family=Poppins:wght@400;600;700&display=swap">
<style>
  :root {
    --stage: #52727f;
    --ink: #263340;
    --aqua: #69d3df;
    --paper: #ffffff;
  }
  html, body {
    margin: 0;
    padding: 0;
    width: 1200px;
    height: 1200px;
    overflow: hidden;
    background: var(--stage);
  }
  .stage {
    display: block;
    width: 1200px;
    height: 1200px;
  }
  .fill-ink { fill: var(--ink); }
  .fill-aqua { fill: var(--aqua); }
  .fill-paper { fill: var(--paper); }
  .hatch { stroke: var(--ink); stroke-width: 7; stroke-linecap: butt; }
  .contact-text {
    font-family: "Poppins", sans-serif;
    font-weight: 400;
    font-size: 37px;
    letter-spacing: 2px;
    fill: var(--ink);
  }
  .job-title {
    font-family: "Poppins", sans-serif;
    font-weight: 600;
    font-size: 34px;
    letter-spacing: 7px;
    fill: var(--ink);
  }
  .person-name {
    font-family: "Poppins", sans-serif;
    font-weight: 700;
    font-size: 78px;
    fill: var(--ink);
  }
  .badge-name {
    font-family: "Poppins", sans-serif;
    font-weight: 600;
    font-size: 46px;
    letter-spacing: 1px;
    fill: var(--aqua);
  }
  .brand-name {
    font-family: "Montserrat", sans-serif;
    font-weight: 600;
    font-size: 92px;
    letter-spacing: 2px;
    fill: var(--paper);
  }
  .pointer-line { stroke: var(--ink); stroke-width: 4; fill: none; }
</style>
</head>
<body>
<svg class="stage" viewBox="0 0 1932 1932" xmlns="http://www.w3.org/2000/svg" aria-label="Velorix business card, front and back">

  <!-- Front side -->
  <g class="card-front">
    <rect class="fill-paper" x="331" y="195" width="1270" height="726"/>
    <path class="fill-aqua" d="M810 195 H1162 L1150 208 Q1135 226 1108 226 H810 Z"/>
    <path class="fill-ink" d="M331 195 H835 L795 245 Q775 268 748 268 H331 Z"/>

    <g class="hatch-top">
      <line class="hatch" x1="1382" y1="195" x2="1370" y2="215"/>
      <line class="hatch" x1="1413" y1="195" x2="1401" y2="215"/>
      <line class="hatch" x1="1444" y1="195" x2="1432" y2="215"/>
      <line class="hatch" x1="1475" y1="195" x2="1463" y2="215"/>
      <line class="hatch" x1="1506" y1="195" x2="1494" y2="215"/>
      <line class="hatch" x1="1537" y1="195" x2="1525" y2="215"/>
      <line class="hatch" x1="1568" y1="195" x2="1556" y2="215"/>
    </g>

    <path class="fill-ink" d="M331 649 H665 Q700 649 700 684 V921 H331 Z"/>
    <path class="fill-aqua" d="M1601 547 H985 Q935 547 905 585 L838 672 Q808 710 760 710 H538 Q432 710 428 815 V921 H1601 Z"/>

    <circle class="fill-paper" cx="1296" cy="515" r="146"/>
    <circle class="fill-ink" cx="1296" cy="506" r="136"/>
    <text class="badge-name" x="1296" y="522" text-anchor="middle">VELORIX</text>

    <g class="contact-list">
      <path class="fill-ink" d="M440 330 Q446 326 450 332 L456 342 Q458 347 453 350 L450 352 Q455 362 464 368 L467 365 Q471 361 476 365 L468 360 L466 362 Q470 366 469 359 L467 360 Z"/>
      <path class="fill-ink" d="M438 329 Q444 325 449 331 L455 341 Q457 346 452 349 L449 351 Q455 362 465 368 L468 365 Q472 361 476 364 L467 356 Z" opacity="0"/>
      <path class="fill-ink" d="M441 328 C436 330 434 336 438 344 C444 356 454 364 464 360 C470 358 471 353 468 350 L462 345 C459 343 456 344 454 347 C449 345 445 341 443 336 C446 334 447 331 445 328 Z"/>
      <text class="contact-text" x="495" y="358">+123-456-7890</text>

      <rect class="fill-ink" x="432" y="399" width="37" height="28" rx="4"/>
      <path d="M435 403 L450 415 L466 403" stroke="#ffffff" stroke-width="4" fill="none"/>
      <text class="contact-text" x="495" y="425">velorix@mailbox.com</text>

      <g fill="none" stroke="#263340" stroke-width="4">
        <circle cx="450" cy="480" r="16"/>
        <ellipse cx="450" cy="480" rx="7" ry="16"/>
        <line x1="434" y1="480" x2="466" y2="480"/>
        <line x1="450" y1="464" x2="450" y2="496"/>
      </g>
      <text class="contact-text" x="495" y="492">123 Anywhere St, Any City</text>
    </g>

    <line class="pointer-line" x1="428" y1="807" x2="586" y2="807"/>
    <circle class="pointer-line" cx="593" cy="807" r="7"/>
    <text class="job-title" x="681" y="820">FOUNDER/OWNER</text>

    <text class="person-name" x="1546" y="787" text-anchor="end">UNKNOWN</text>
    <text class="person-name" x="1546" y="862" text-anchor="end">PERSON</text>

    <g class="hatch-bottom">
      <line class="hatch" x1="642" y1="901" x2="630" y2="921"/>
      <line class="hatch" x1="673" y1="901" x2="661" y2="921"/>
      <line class="hatch" x1="704" y1="901" x2="692" y2="921"/>
      <line class="hatch" x1="735" y1="901" x2="723" y2="921"/>
      <line class="hatch" x1="766" y1="901" x2="754" y2="921"/>
      <line class="hatch" x1="797" y1="901" x2="785" y2="921"/>
      <line class="hatch" x1="828" y1="901" x2="816" y2="921"/>
    </g>
  </g>

  <!-- Back side -->
  <g class="card-back">
    <rect class="fill-ink" x="331" y="1011" width="1270" height="726"/>
    <path class="fill-aqua" d="M331 1011 H835 L795 1061 Q775 1084 748 1084 H331 Z"/>
    <path class="fill-aqua" d="M1601 1362 H985 Q935 1362 905 1400 L838 1488 Q808 1526 760 1526 H538 Q432 1526 428 1631 V1737 H1601 Z"/>

    <circle class="fill-aqua" cx="597" cy="1310" r="92"/>
    <text class="brand-name" x="1520" y="1236" text-anchor="end">VELORIX</text>
  </g>
</svg>
</body>
</html>
```